Looking to design a new sign for our church.

Looking for a new sign
4 x 8 feet dimension
We are renaming the church "Medlow Ridge Community Church"
looking for legible graphics
Would like some type of backdrop being a family tree (oak) / open to other ideas as you are led
I have included a pic of the old sign for your review
would like to incorporate our ministry logo on the lower right hand corner of the sign / see file attached

```html
<!DOCTYPE html>
<html lang="en">
<head>
<meta charset="utf-8">
<title>Medlow Ridge Community Church – Sign</title>
<link href="https://fonts.googleapis.com/css2?family=Archivo+Black&family=Oswald:wght@500&family=Yellowtail&display=swap" rel="stylesheet">
<style>
  :root {
    --page-bg: #e9e6e1;
    --ink-white: #ffffff;
    --shadow-navy: #2a2466;
    --sky-purple: #3a1a45;
    --sky-plum: #6b2d4f;
    --sky-orange: #e5792a;
    --sky-gold: #f5c43c;
    --ground-brown: #3a2218;
  }
  * { margin: 0; padding: 0; box-sizing: border-box; }
  html, body {
    width: 1093px; height: 1200px; overflow: hidden;
    background: var(--page-bg);
  }
  .sign {
    position: absolute;
    left: 0; top: 327px;
    width: 1093px; height: 546px;
    overflow: hidden;
  }
  .sign__backdrop { position: absolute; inset: 0; width: 100%; height: 100%; }
  .sign__title {
    position: absolute;
    left: 178px; top: 22px;
    font-family: "Archivo Black", sans-serif;
    font-size: 98px; line-height: 1;
    letter-spacing: -2px;
    color: var(--ink-white);
    text-shadow: 4px 4px 0 var(--shadow-navy);
    white-space: nowrap;
  }
  .sign__script {
    position: absolute;
    left: 470px; top: 118px;
    font-family: "Yellowtail", cursive;
    font-size: 118px; line-height: 1;
    color: var(--ink-white);
    white-space: nowrap;
  }
  .sign__church {
    position: absolute;
    left: 464px; top: 240px;
    font-family: "Archivo Black", sans-serif;
    font-size: 98px; line-height: 1;
    letter-spacing: -2px;
    color: var(--ink-white);
    text-shadow: 4px 4px 0 var(--shadow-navy);
  }
  .sign__times {
    position: absolute;
    left: 468px; top: 386px;
    list-style: none;
    font-family: "Oswald", sans-serif;
    font-weight: 500;
    font-size: 38px; line-height: 45px;
    color: var(--ink-white);
    white-space: nowrap;
  }
  .ministry-mark {
    position: absolute;
    left: 944px; top: 450px;
    width: 120px;
    display: flex; flex-direction: column; align-items: center; gap: 8px;
  }
  .ministry-mark__dot {
    width: 30px; height: 30px; border-radius: 50%;
    background: var(--ink-white);
  }
  .ministry-mark__name {
    font-family: "Oswald", sans-serif;
    font-weight: 500;
    font-size: 18px; line-height: 20px;
    text-align: center;
    color: var(--ink-white);
  }
</style>
</head>
<body>
  <main class="sign">
    <svg class="sign__backdrop" viewBox="0 0 1093 546" preserveAspectRatio="none" role="img" aria-label="Sunset sky with a silhouetted oak tree and a wooden cross standing on a rocky hill">
      <defs>
        <radialGradient id="sunset-glow" cx="0.33" cy="0.62" r="0.85">
          <stop offset="0" stop-color="var(--sky-gold)"/>
          <stop offset="0.3" stop-color="var(--sky-orange)"/>
          <stop offset="0.62" stop-color="var(--sky-plum)"/>
          <stop offset="1" stop-color="var(--sky-purple)"/>
        </radialGradient>
        <linearGradient id="hill-fade" x1="0" y1="0" x2="0" y2="1">
          <stop offset="0.78" stop-color="var(--ground-brown)" stop-opacity="0"/>
          <stop offset="1" stop-color="var(--ground-brown)"/>
        </linearGradient>
        <linearGradient id="tree-shade" x1="0" y1="0" x2="1" y2="0">
          <stop offset="0" stop-color="#1e0f12" stop-opacity="0.85"/>
          <stop offset="0.3" stop-color="#1e0f12" stop-opacity="0"/>
        </linearGradient>
      </defs>
      <rect width="1093" height="546" fill="url(#sunset-glow)"/>
      <rect width="1093" height="546" fill="url(#tree-shade)"/>
      <rect width="1093" height="546" fill="url(#hill-fade)"/>
    </svg>

    <h1 class="sign__title">MEDLOW RIDGE</h1>
    <p class="sign__script">Community</p>
    <p class="sign__church">CHURCH</p>

    <ul class="sign__times">
      <li>10:30 AM WORSHIP SERVICE</li>
      <li>9:30 AM SUNDAY SCHOOL</li>
      <li>6:00 AM WEDNESDAY SERVICE</li>
    </ul>

    <div class="ministry-mark">
      <span class="ministry-mark__dot"></span>
      <span class="ministry-mark__name">Ridgeway<br>Missions</span>
    </div>
  </main>
</body>
</html>
```